Website design and Setup for Real Estate Firm and Going Live

We are a commercial real estate investment firm and are looking for a 6 page website which is informational only. Some text and graphics on each page. We would want the designer to code and launch the website. This website needs to be corporate looking as well as innovative. We are setting up the website on webnook.

The first page will be a home page with generic commercial real estate look with a link to the following 5 pages on page 1. So page one (the Home Page should have a commercial real estate look with the text linking to the following pages. Page 2 "About Us" with 3 paragraphs describing our firm. Page 3 "Our Platform" with another few paragraphs on due diligence, acquisitions, financing, and management.

Page 4 is "Our Team" highlighting several manager profiles. Page 5 is our "investment Portfolio portal" which will be password protected so not a lot of text, only general graphics and anyone viewing the site casually won't get into the backend, Page 6 is the contact us page. All of the content will be uploaded shortly.

The project includes setting up hyperlinks in the website as well rotating images etc and a final complete live online product. We do not expect to pay for any stock images.

Target Market(s)

Investors, Real Estate Professionals, Brokerages

Industry/Entity Type

Real Estate

Coding

Coded - Design and coding required

Number of Pages Required

5+ page

Requirements
Must have
• Corporate cutting edge design, suitable for a financial corporation.

```html
<!DOCTYPE html>
<html lang="en">
<head>
<meta charset="utf-8">
<title>Harlow Crest Realty</title>
<link href="https://fonts.googleapis.com/css2?family=Titillium+Web:wght@300;400;600;700&family=Lato:wght@400;700&display=swap" rel="stylesheet">
<style>
:root{
  --navy:#1a2479;
  --navy-deep:#151d66;
  --accent:#2c7fc2;
  --text:#444a55;
  --white:#ffffff;
  --footer:#121212;
  --footer-text:#d9d9d9;
  --rule:#d8dbe3;
}
*{box-sizing:border-box;margin:0;padding:0}
html,body{width:1200px;height:3688px;overflow:hidden}
body{position:relative;font-family:'Lato',sans-serif;color:var(--text);background:var(--white)}
.abs{position:absolute}
section,footer{position:absolute;left:0;width:1200px;overflow:hidden}

/* hero */
.hero{top:0;height:643px}
.hero-photo{position:absolute;inset:0;background:linear-gradient(180deg,#3c4a6a 0%,#5b6f8e 35%,#4d5e5a 65%,#2f3f2a 100%)}
.hero-shade{position:absolute;inset:0;background:rgba(20,28,70,.35)}
.brand{left:112px;top:42px;font-family:'Titillium Web',sans-serif;font-weight:600;font-size:30px;color:var(--white);letter-spacing:.2px}
.nav{right:112px;top:50px;display:flex;gap:14px;font-family:'Titillium Web',sans-serif;font-weight:600;font-size:17px;color:var(--white)}
.hero-title{left:0;width:1200px;top:252px;text-align:center;font-family:'Titillium Web',sans-serif;font-weight:600;font-size:46px;line-height:60px;color:var(--white)}
.hero-rule{height:2px;background:var(--white);top:340px;width:128px}
.btn{display:flex;align-items:center;justify-content:center;background:var(--navy);color:var(--white);font-family:'Titillium Web',sans-serif;font-weight:600;font-size:17px;letter-spacing:.3px}
.btn.outlined{border:1px solid #5d7ac0}
.scroll-icon{left:586px;top:585px}

/* about */
.about{top:643px;height:563px;background:var(--white)}
.frame{left:122px;top:84px;width:269px;height:260px;border:2px solid var(--accent)}
.photo-building{left:112px;top:96px;width:268px;height:342px;background:linear-gradient(160deg,#33466e 0%,#4c618b 40%,#8c7b4c 75%,#3a3a35 100%)}
.photo-portrait{left:305px;top:289px;width:175px;height:181px;border:3px solid var(--white);background:linear-gradient(160deg,#2a4a72,#18263f)}
.eyebrow{font-family:'Titillium Web',sans-serif;font-weight:600;font-size:24px;color:var(--accent)}
.eyebrow-line{height:2px;background:var(--accent)}
.about-title{left:563px;top:128px;font-family:'Titillium Web',sans-serif;font-weight:400;font-size:31px;color:var(--navy)}
.about-text{left:563px;top:184px;width:525px;font-size:17px;line-height:30px;color:var(--text)}

/* services */
.services{top:1206px;height:658px;background:var(--navy)}
.sec-label{left:0;width:1200px;text-align:center;font-family:'Titillium Web',sans-serif;font-weight:600;font-size:26px}
.sec-title{left:0;width:1200px;text-align:center;font-family:'Titillium Web',sans-serif;font-weight:400;font-size:34px}
.dash{height:2px}
.card{top:230px;width:286px;height:332px;background:var(--white)}
.card svg{position:absolute;left:24px;top:32px}
.card-title{position:absolute;left:26px;top:120px;font-family:'Titillium Web',sans-serif;font-weight:700;font-size:19px;line-height:28px;color:var(--navy)}
.card-text{position:absolute;left:26px;top:156px;width:255px;font-size:17px;line-height:30px;color:var(--text);white-space:nowrap}
.read-more{font-family:'Titillium Web',sans-serif;font-weight:700;font-size:16px;line-height:20px;color:var(--navy);letter-spacing:.2px}
.card .read-more{position:absolute;left:24px;top:282px}

/* blog */
.blog{top:1864px;height:861px;background:var(--white)}
.post-photo{left:127px;top:222px;width:572px;height:308px;background:linear-gradient(180deg,#8fb1d8 0%,#c9d9ea 35%,#3d5a8a 55%,#8e98a6 85%,#6e7a6a 100%)}
.avatar{left:127px;top:552px;width:28px;height:28px;border-radius:50%;background:#8f9aad;border:1px solid #c3c8d2}
.meta{font-size:13px;color:var(--navy);font-family:'Titillium Web',sans-serif}
.post-rule{left:127px;top:590px;width:575px;height:1px;background:var(--rule)}
.post-title{left:130px;top:612px;font-family:'Titillium Web',sans-serif;font-weight:600;font-size:19px;color:var(--navy)}
.post-text{left:130px;top:648px;width:560px;font-size:16px;line-height:30px;color:var(--text)}
.side-post{left:770px;width:303px;height:151px}
.side-photo{position:absolute;inset:0}
.side-caption{position:absolute;left:0;bottom:0;width:100%;height:62px;background:rgba(25,25,25,.78);padding:4px 20px;font-size:15px;line-height:27px;color:#e8e8e8;white-space:nowrap}

/* contact */
.contact{top:2725px;height:626px}
.contact-photo{position:absolute;inset:0;background:linear-gradient(160deg,#4a5e8e 0%,#3a4d84 45%,#2f4075 100%)}
.contact-shade{position:absolute;inset:0;background:rgba(34,52,140,.55)}
.contact-lead{left:0;width:1200px;top:165px;text-align:center;font-weight:700;font-size:17px;line-height:30px;color:var(--white)}
.field{background:var(--white);display:flex;align-items:center;gap:9px;padding-left:12px;font-size:17px;color:#777;border:1px solid #c9cde0}
.field.tall{align-items:flex-start;padding-top:12px}

/* footer */
.footer{top:3351px;height:337px;background:var(--footer)}
.col-title{font-family:'Titillium Web',sans-serif;font-weight:600;font-size:17px;color:var(--white);top:79px}
.col-list{top:112px;list-style:none;font-size:16px;line-height:30px;color:var(--footer-text)}
.col-list li{display:flex;align-items:center;gap:12px}
.col-rule{top:61px;width:1px;height:179px;background:#3a3a3a}
.copyright{left:0;width:1200px;top:297px;text-align:center;font-size:16px;color:var(--footer-text)}
</style>
</head>
<body>

<section class="hero">
  <div class="hero-photo" role="img" aria-label="Modern glass office tower with skybridge and trees in the foreground"></div>
  <div class="hero-shade"></div>
  <div class="abs brand">HARLOW CREST REALTY</div>
  <nav class="abs nav"><span>HOME</span><span>ABOUT US</span><span>OUR APPROACH</span><span>PORTFOLIO</span><span>BLOG</span><span>CONTACT</span></nav>
  <h1 class="abs hero-title">FIND HIGHEST QUALITYQ REAL<br>ESTATE</h1>
  <div class="abs hero-rule" style="left:380px"></div>
  <div class="abs hero-rule" style="left:692px"></div>
  <div class="abs btn outlined" style="left:517px;top:401px;width:166px;height:59px">GET STARTED</div>
  <svg class="abs scroll-icon" width="28" height="36" viewBox="0 0 28 36" fill="none" stroke="#fff" stroke-width="2"><rect x="2" y="2" width="24" height="32" rx="12"/><path d="M14 9v13M9 17l5 5 5-5"/></svg>
</section>

<section class="about">
  <div class="abs frame"></div>
  <div class="abs photo-building" role="img" aria-label="Glass office building lit at dusk under a cloudy sky"></div>
  <div class="abs photo-portrait" role="img" aria-label="Portrait of the firm's principal in a dark suit"></div>
  <div class="abs eyebrow" style="left:563px;top:92px">ABOUT</div>
  <div class="abs eyebrow-line" style="left:648px;top:114px;width:95px"></div>
  <h2 class="abs about-title">HARLOW CREST REALTY</h2>
  <p class="abs about-text">Lorem ipsum dolor sit amet, consectetur adipiscing elit, sed do eiusmod tempor incididunt ut labore et dolore magna aliqua. Ut enim ad minim veniam, quis nostrud exercitation ullamco laboris nisi ut aliquip ex ea commodo consequat. Duis aute irure dolor in reprehenderit in voluptate velit esse cillum dolore eu fugiat nulla pariatur.</p>
  <div class="abs btn" style="left:563px;top:400px;width:165px;height:58px">GET STARTED</div>
</section>

<section class="services">
  <div class="abs dash" style="left:505px;top:97px;width:30px;background:#fff"></div>
  <div class="abs sec-label" style="top:74px;color:#fff">SERVICES</div>
  <div class="abs dash" style="left:664px;top:97px;width:30px;background:#fff"></div>
  <h2 class="abs sec-title" style="top:112px;color:#fff">WHAT WE DO</h2>

  <svg class="abs" style="left:38px;top:386px" width="40" height="20" viewBox="0 0 40 20" fill="none" stroke="#fff" stroke-width="2"><path d="M39 10H2M10 2L2 10l8 8"/></svg>
  <svg class="abs" style="left:1126px;top:386px" width="40" height="20" viewBox="0 0 40 20" fill="none" stroke="#fff" stroke-width="2"><path d="M1 10h37M30 2l8 8-8 8"/></svg>

  <div class="abs card" style="left:137px">
    <svg width="66" height="64" viewBox="0 0 66 64" fill="none" stroke="#2c5fb0" stroke-width="2.2"><path d="M4 40l12-10 10 4 10-6 12 8 12-4"/><path d="M18 48l8 6 8-6 8 6 8-6"/><path d="M26 4h12v12H26zM40 8h10M44 2l6 6-6 6"/><path d="M30 22v6M36 20v8"/></svg>
    <div class="card-title">ACQUISITION</div>
    <p class="card-text">Sed ut perspiciatis unde omn<br>iste natus error sit voluptate<br>m accusantium doloremque<br>laudantium.</p>
    <div class="read-more">READ MORE &nbsp;»</div>
  </div>
  <div class="abs card" style="left:457px">
    <svg width="66" height="64" viewBox="0 0 66 64" fill="none" stroke="#2c5fb0" stroke-width="2.2"><circle cx="32" cy="32" r="18"/><circle cx="32" cy="32" r="11"/><path d="M32 4v8M32 52v8M4 32h8M52 32h8M12 12l6 6M46 46l6 6M12 52l6-6M46 18l6-6"/><path d="M27 32l4 4 7-8"/></svg>
    <div class="card-title">DEVELOPMENT</div>
    <p class="card-text">Sed ut perspiciatis unde omn<br>iste natus error sit voluptate<br>m accusantium doloremque<br>laudantium.</p>
    <div class="read-more">READ MORE &nbsp;»</div>
  </div>
  <div class="abs card" style="left:779px">
    <svg width="72" height="64" viewBox="0 0 72 64" fill="none" stroke="#2c5fb0" stroke-width="2.2"><path d="M2 62h68"/><path d="M8 62V50h8v12M22 62V42h8v20M36 62V34h8v28M50 62V26h8v36"/><path d="M6 44l14-10 12 4 18-14"/><circle cx="58" cy="10" r="8"/><path d="M58 5v10M55 8h5M55 12h5"/></svg>
    <div class="card-title">FINANCING</div>
    <p class="card-text">Sed ut perspiciatis unde omn<br>iste natus error sit voluptate<br>m accusantium doloremque<br>laudantium.</p>
    <div class="read-more">READ MORE &nbsp;»</div>
  </div>
</section>

<section class="blog">
  <div class="abs dash" style="left:529px;top:106px;width:30px;background:var(--accent)"></div>
  <div class="abs sec-label" style="top:83px;color:var(--accent)">BLOG</div>
  <div class="abs dash" style="left:644px;top:106px;width:30px;background:var(--accent)"></div>
  <h2 class="abs sec-title" style="top:124px;color:var(--navy)">LATEST NEWS</h2>

  <div class="abs post-photo" role="img" aria-label="Blue glass and white office building under a cloudy sky"></div>
  <div class="abs avatar" role="img" aria-label="Author avatar"></div>
  <div class="abs meta" style="left:161px;top:558px">BY MARK T.</div>
  <div class="abs meta" style="right:500px;top:558px">ON DEC 24, 2021</div>
  <div class="abs post-rule"></div>
  <h3 class="abs post-title">LOREM IPSUM DOLOR SIT AMET, CONSECTETUR ADI</h3>
  <p class="abs post-text">Sed ut perspiciatis unde omnis iste natus error sit voluptatem accusantium doloremque laudantium, totam rem aperiam, eaque ipsa quae ab illo inventore veritatis.</p>
  <div class="abs read-more" style="left:130px;top:752px">READ MORE &nbsp;»</div>

  <div class="abs side-post" style="top:222px">
    <div class="side-photo" role="img" aria-label="Hands holding a phone at an office desk" style="background:linear-gradient(135deg,#6f6a63,#b9b4aa 50%,#3a3a38)"></div>
    <div class="side-caption">Lorem ipsum dolor sit amet, conse<br>tetur adipiscing elit.</div>
  </div>
  <div class="abs side-post" style="top:387px">
    <div class="side-photo" role="img" aria-label="Two colleagues reviewing a tablet in an office" style="background:linear-gradient(135deg,#a0876a,#c9d2dc 50%,#2c3444)"></div>
    <div class="side-caption">Lorem ipsum dolor sit amet, conse<br>tetur adipiscing elit.</div>
  </div>
  <div class="abs side-post" style="top:553px">
    <div class="side-photo" role="img" aria-label="Business handshake across a table" style="background:linear-gradient(135deg,#2c3240,#9aa3b0 55%,#3a3f4a)"></div>
    <div class="side-caption">Lorem ipsum dolor sit amet, conse<br>tetur adipiscing elit.</div>
  </div>
  <div class="abs read-more" style="left:854px;top:735px">SEE ALL BLOGS &nbsp;»</div>
</section>

<section class="contact">
  <div class="contact-photo" role="img" aria-label="Aerial view of an office park with parking lots and trees"></div>
  <div class="contact-shade"></div>
  <div class="abs dash" style="left:477px;top:92px;width:60px;background:#fff"></div>
  <div class="abs sec-label" style="top:70px;color:#fff">CONTACT</div>
  <div class="abs dash" style="left:656px;top:92px;width:60px;background:#fff"></div>
  <h2 class="abs sec-title" style="top:108px;color:#fff">ASK THE EXPERT</h2>
  <p class="abs contact-lead">Nam libero tempore, cum soluta nobis est eligendi optio<br>cumque nihil impedit quo minus id.</p>

  <div class="abs field" style="left:324px;top:254px;width:272px;height:46px"><svg width="12" height="13" viewBox="0 0 12 13" fill="#444"><circle cx="6" cy="3.5" r="3"/><path d="M0 13c0-4 2.5-6 6-6s6 2 6 6z"/></svg>Name</div>
  <div class="abs field" style="left:604px;top:254px;width:272px;height:46px"><svg width="13" height="10" viewBox="0 0 13 10" fill="#444"><rect width="13" height="10" rx="1"/><path d="M0 1l6.5 5L13 1" stroke="#fff" fill="none"/></svg>Email</div>
  <div class="abs field" style="left:324px;top:311px;width:272px;height:46px"><svg width="12" height="12" viewBox="0 0 12 12" fill="#444"><path d="M2 0l3 3-1.5 2a7 7 0 003.5 3.5L9 7l3 3-2 2C4 12 0 8 0 2z"/></svg>Phone</div>
  <div class="abs field" style="left:604px;top:311px;width:272px;height:46px"><svg width="13" height="13" viewBox="0 0 13 13" fill="none" stroke="#444" stroke-width="2"><circle cx="6.5" cy="6.5" r="3"/><path d="M6.5 0v2.5M6.5 10.5V13M0 6.5h2.5M10.5 6.5H13"/></svg>Services</div>
  <div class="abs field tall" style="left:324px;top:368px;width:552px;height:102px"><svg width="12" height="12" viewBox="0 0 12 12" fill="#444" style="margin-top:4px"><path d="M9 0l3 3-8 8H1V8z"/></svg>Message</div>
  <div class="abs btn outlined" style="left:517px;top:488px;width:166px;height:59px">SUBMIT</div>
</section>

<footer class="footer">
  <div class="abs col-title" style="left:116px">QUICK LINKS</div>
  <ul class="abs col-list" style="left:117px"><li>Home</li><li>About</li><li>Services</li><li>Blog</li><li>Portfolio</li></ul>
  <div class="abs col-rule" style="left:282px"></div>

  <div class="abs col-title" style="left:378px">BUSINESS HOURS</div>
  <ul class="abs col-list" style="left:379px"><li>mon- fri</li><li>9 am - 7 pm</li><li>&nbsp;</li><li>sat- sun</li><li>11 am - 5 pm</li></ul>
  <div class="abs col-rule" style="left:558px"></div>

  <div class="abs col-title" style="left:640px">CONTACT US</div>
  <ul class="abs col-list" style="left:641px;line-height:37px;top:105px">
    <li><svg width="12" height="16" viewBox="0 0 12 16" fill="#fff"><path d="M6 0a6 6 0 016 6c0 4-6 10-6 10S0 10 0 6a6 6 0 016-6z"/><circle cx="6" cy="6" r="2" fill="#121212"/></svg>Address comes here</li>
    <li><svg width="13" height="13" viewBox="0 0 12 12" fill="#fff"><path d="M2 0l3 3-1.5 2a7 7 0 003.5 3.5L9 7l3 3-2 2C4 12 0 8 0 2z"/></svg>+1 (123) 456-789</li>
    <li><svg width="15" height="14" viewBox="0 0 15 14" fill="#fff"><rect x="3" y="0" width="9" height="4"/><rect x="0" y="5" width="15" height="6" rx="1"/><rect x="3" y="9" width="9" height="5" stroke="#121212"/></svg>+1 (123) 789-456</li>
    <li><svg width="14" height="11" viewBox="0 0 13 10" fill="#fff"><rect width="13" height="10" rx="1"/><path d="M0 1l6.5 5L13 1" stroke="#121212" fill="none"/></svg>info@harlowcrest.us</li>
  </ul>
  <div class="abs col-rule" style="left:878px"></div>

  <div class="abs col-title" style="left:955px">OTHERS</div>
  <ul class="abs col-list" style="left:956px"><li>Tearms &amp; Services</li><li>Privacy Policy</li><li>FAQs</li><li>Contact</li></ul>

  <div class="abs copyright">©2021 Harlow Crest Realty. All Rights Reserved.</div>
</footer>

</body>
</html>
```